Small animal veterinary clinic needs a new web site design

We need a new web site design for Harlowe Veterinary Clinic. The clinic performs medicine, surgery, and wellness care for cats and dogs. We have been in business for over 50 years so we want to project stability, reliability, class, elegance, and professionalism. We also want to convey that we have modern facilities and services and perform high quality medicine.
The current web site has been in place for many years and looks stale but for reference it is at http://www.harlowevc-example.com. We will be re-writing most of the content and looking to add additional pages, videos, downloadable documents (forms, brochures, marketing materials, etc.) The new owners prefer a more classy, modern look. Some vet clinic sites we like are http://pennfrolt.com and http://curaplumtails.com. We like a nice, clean, fresh, interactive interface.
Our new logo is attached. We want the color scheme of the web site to be complementary to the colors in the logo, especially the blue and green. The purple color of the text should just be used for accent. Upon request and if necessary, I can supply the Adobe Illustrator source file for the logo.
We are looking for a set of page designs - a great, eye-catching home page and 2-3 content page layouts we can use to create content pages with our own text and other content. Navigation design is very important as well. Again, we can fill in the content of the navigation links but I would like a nice, easy-to-use, logical navigation design. If you want some content or navigation links to use as reference during your design phase, feel free to pull whatever content or navigation you want from our existing web site. I am not looking for just images, I would like actual page files - HTML, CSS, etc.
Thanks and good luck!
Target Market(s)
We cater to pet owners across a wide age range. Socio-economic status of our customers is middle class and above. We do not target price shoppers.
Industry/Entity Type
Veterinary
Colors
Designer to choose colors to be used in the design.
Requirements
Must have
- Must look professional, clean, and modern. We are looking for simple but elegant design and navigation. 1 home page design, 2-3 content page designs delivered with code (HTML & CSS).
Nice to have
- When HTML/CSS is delivered, it would be awesome if it were mobile ready as well.
Should not have
- Colors that are too bold. Layout that is too complex.

```html
<!DOCTYPE html>
<html lang="en">
<head>
<meta charset="utf-8">
<title>Harlowe Veterinary Clinic</title>
<link rel="stylesheet" href="https://fonts.googleapis.com/css2?family=Roboto:ital,wght@0,400;0,500;0,700;1,400&family=Righteous&family=Cinzel:wght@500&display=swap">
<style>
:root{
  --green-deep:#3fae5a;
  --green-mid:#5cc46e;
  --green-light:#9ee6b0;
  --headline:#2a9f3e;
  --band:#e1f5d2;
  --white:#ffffff;
  --ink:#3a3a3a;
  --ink-soft:#666666;
  --dark:#33373b;
  --footer:#353535;
  --nav-bg:rgba(40,120,60,.45);
  --nav-active:rgba(255,255,255,.28);
}
*{box-sizing:border-box;margin:0;padding:0}
html,body{width:700px;height:1200px;overflow:hidden;background:var(--white)}
body{position:relative;font-family:"Roboto",Arial,sans-serif;color:var(--ink)}
.abs{position:absolute}

.masthead{left:0;top:0;width:700px;height:180px;
  background:linear-gradient(90deg,var(--green-deep) 0%,var(--green-mid) 30%,#8fe3d0 50%,var(--green-mid) 72%,#7fd765 100%)}
.brand{left:35px;top:18px;width:130px;height:105px;text-align:center;color:var(--white)}
.brand-mark{display:block;width:58px;height:58px;margin:0 auto 10px;border:2px solid var(--white);border-radius:50%}
.brand-name{font-family:"Cinzel",serif;font-weight:500;font-size:17px;letter-spacing:.5px;line-height:1}
.brand-tag{font-family:"Cinzel",serif;font-weight:500;font-size:8px;margin-top:3px}
.appointment{right:62px;top:24px;color:var(--white);font-size:9px;line-height:14px}
.appointment em{display:block;font-style:italic}
.appointment svg{vertical-align:-1px;margin-right:3px}

.main-nav{left:0;top:140px;width:700px;height:40px;background:var(--nav-bg)}
.main-nav a{position:absolute;top:0;height:40px;line-height:40px;color:var(--white);
  font-size:10px;font-weight:500;text-decoration:none;letter-spacing:.2px}
.main-nav a.is-active{height:55px;background:var(--nav-active);padding:0 10px}

.hero{left:0;top:180px;width:700px;height:203px;background:var(--white)}
.hero-photo{left:0;top:8px;width:295px;height:192px;
  background:radial-gradient(ellipse at 30% 45%,#c98a45 0%,#d9a465 35%,#b8a996 60%,rgba(255,255,255,0) 80%)}
.hero-title{left:315px;top:6px;font-family:"Righteous",sans-serif;color:var(--headline);
  font-size:46px;line-height:50px;letter-spacing:.5px}

.band{left:0;width:700px;background:var(--band)}
.card{background:var(--white);text-align:center}
.card h2{font-weight:400;font-size:15px;color:var(--ink);margin-top:20px;letter-spacing:.2px}
.card p{font-size:7.5px;color:var(--ink-soft);line-height:10.5px;margin-top:14px}
.arrow-btn{position:absolute;right:0;bottom:0;width:27px;height:21px;background:var(--dark)}
.arrow-btn svg{position:absolute;left:10px;top:7px}

.section-title{font-size:14.5px;font-weight:400;color:var(--ink);letter-spacing:.2px}
.staff-card{width:200px}
.staff-photo{position:absolute;left:0;top:0;width:41px;height:31px;border-radius:50%;
  background:linear-gradient(135deg,#7a6a5a,#cfc2b0)}
.staff-name{position:absolute;left:95px;top:1px;font-size:9.5px;color:#555}
.staff-role{position:absolute;left:108px;top:21px;font-size:7px;color:#777}
.staff-text{position:absolute;left:0;top:42px;width:190px;font-size:7.5px;line-height:10px;color:var(--ink-soft)}
.read-more{position:absolute;left:17px;top:78px;width:97px;height:20px;background:var(--dark);
  color:var(--white);font-size:7.5px;text-align:center;line-height:20px;letter-spacing:.4px;
  box-shadow:0 0 0 1px #cfe6c5}

.video-thumb{left:35px;top:819px;width:198px;height:85px;
  background:linear-gradient(90deg,#7d6f5f 0%,#b8a58c 40%,#8a8f95 70%,#5f666d 100%)}
.play{left:88px;top:31px;width:22px;height:22px;border-radius:50%;background:rgba(255,255,255,.45)}
.zoom{right:0;bottom:0;width:23px;height:17px;background:var(--dark)}
.caption-title{left:35px;top:913px;font-size:9.5px;font-weight:500;color:#444}
.caption-sub{left:35px;top:932px;font-size:7px;color:#777}

.about{left:0;top:978px;width:700px;height:136px;
  background:radial-gradient(ellipse at 50% 40%,#5a5f5c 0%,#2e302f 60%,#1e1f1f 100%)}
.about h2{position:absolute;left:0;top:40px;width:700px;text-align:center;color:var(--white);font-weight:400;font-size:12px}
.about p{position:absolute;left:35px;top:67px;width:630px;color:#e8e8e8;font-size:7.5px;line-height:10.5px}

.site-footer{left:0;top:1114px;width:700px;height:86px;background:var(--footer)}
.footer-links{position:absolute;left:35px;top:33px;color:#e5e5e5;font-size:7.5px;line-height:10px}
.social{position:absolute;top:27px;width:25px;height:19px}
.to-top{position:absolute;left:665px;top:31px;width:25px;height:22px;background:var(--white);
  font-size:8px;text-align:center;line-height:22px;color:#333}
</style>
</head>
<body>

<header class="abs masthead">
  <div class="abs brand">
    <span class="brand-mark"></span>
    <div class="brand-name">HARLOWE</div>
    <div class="brand-tag">veterinary clinic</div>
  </div>
  <div class="abs appointment">
    <em>Request an Appointment</em>
    <svg width="8" height="8" viewBox="0 0 24 24"><path fill="#fff" d="M6.6 10.8a15 15 0 0 0 6.6 6.6l2.2-2.2c.3-.3.7-.4 1-.2 1.1.4 2.3.6 3.6.6.6 0 1 .4 1 1V20c0 .6-.4 1-1 1A17 17 0 0 1 3 4c0-.6.4-1 1-1h3.5c.6 0 1 .4 1 1 0 1.3.2 2.5.6 3.6.1.3 0 .7-.2 1z"/></svg>+1 800 555 0147
  </div>
</header>

<nav class="abs main-nav">
  <a class="is-active" href="#" style="left:182px">OUR PRACTICES</a>
  <a href="#" style="left:295px">OUR STAFF</a>
  <a href="#" style="left:373px">SERVICES</a>
  <a href="#" style="left:445px">CONTACT US</a>
</nav>

<section class="abs hero">
  <div class="abs hero-photo" role="img" aria-label="Photo of a golden dog lying beside a tabby cat"></div>
  <h1 class="abs hero-title" style="font-weight:400">Your pet will<br>Love you<br>for<br>this “Forever”.</h1>
</section>

<section class="abs band" style="top:383px;height:189px">
  <article class="abs card" style="left:35px;top:30px;width:190px;height:98px">
    <h2>LATEST NEWS</h2>
    <p>We Offer Pet Portals!</p>
    <span class="arrow-btn"><svg width="6" height="8" viewBox="0 0 6 8"><path d="M1 1l3 3-3 3" stroke="#fff" stroke-width="1.4" fill="none"/></svg></span>
  </article>
  <article class="abs card" style="left:248px;top:30px;width:190px;height:119px">
    <h2>LINKS</h2>
    <p>Vellora Nutrition<br>Please visit our website for Boarding and<br>Grooming</p>
    <span class="arrow-btn"><svg width="6" height="8" viewBox="0 0 6 8"><path d="M1 1l3 3-3 3" stroke="#fff" stroke-width="1.4" fill="none"/></svg></span>
  </article>
  <article class="abs card" style="left:461px;top:30px;width:190px;height:130px">
    <h2>CARE GUIDES</h2>
    <p>Exercising Your Dog<br>Feline Obesity<br>Radiography<br>Spaying or Neutering Your Pet</p>
    <span class="arrow-btn"><svg width="6" height="8" viewBox="0 0 6 8"><path d="M1 1l3 3-3 3" stroke="#fff" stroke-width="1.4" fill="none"/></svg></span>
  </article>
</section>

<section class="abs" style="left:0;top:572px;width:700px;height:190px">
  <h2 class="abs section-title" style="left:35px;top:26px">MOST CARING STAFF</h2>
  <div class="abs staff-card" style="left:35px;top:57px">
    <div class="staff-photo" role="img" aria-label="Staff portrait"></div>
    <div class="staff-name">PERSPICIATIS</div>
    <div class="staff-role">TOTAM REM APERIAM</div>
    <p class="staff-text">Eaque ipsa quae ab illo inventore veritatis et quasi architecto beatae vitae dicta sunt explicabo.</p>
    <div class="read-more">READ MORE</div>
  </div>
  <div class="abs staff-card" style="left:248px;top:57px">
    <div class="staff-photo" role="img" aria-label="Staff portrait"></div>
    <div class="staff-name">PERSPICIATIS</div>
    <div class="staff-role">TOTAM REM APERIAM</div>
    <p class="staff-text">Eaque ipsa quae ab illo inventore veritatis et quasi architecto beatae vitae dicta sunt explicabo.</p>
    <div class="read-more">READ MORE</div>
  </div>
  <div class="abs staff-card" style="left:461px;top:57px">
    <div class="staff-photo" role="img" aria-label="Staff portrait"></div>
    <div class="staff-name">PERSPICIATIS</div>
    <div class="staff-role">TOTAM REM APERIAM</div>
    <p class="staff-text">Eaque ipsa quae ab illo inventore veritatis et quasi architecto beatae vitae dicta sunt explicabo.</p>
    <div class="read-more">READ MORE</div>
  </div>
</section>

<section class="abs band" style="top:762px;height:216px">
  <h2 class="abs section-title" style="left:35px;top:27px">MARCUS AND LENA WHITCOMBE SHARE THEIR STORY</h2>
</section>
<div class="abs video-thumb" role="img" aria-label="Video still of two clients telling their story">
  <span class="abs play"></span>
  <span class="abs zoom"><svg width="23" height="17" viewBox="0 0 23 17"><circle cx="11" cy="8" r="3" stroke="#fff" stroke-width="1.3" fill="none"/><path d="M13.2 10.2l2.5 2.5" stroke="#fff" stroke-width="1.3"/></svg></span>
</div>
<div class="abs caption-title">PERSPICIATIS</div>
<div class="abs caption-sub">TOTAM REM APERIAM</div>

<section class="abs about" role="img" aria-label="Blurred photo of the clinic interior">
  <h2>WHAT WE DO</h2>
  <p>Harlowe Veterinary Clinic is a full-service veterinary medical hospital, located in Alder Springs, SC. The professional and courteous staff at Harlowe Veterinary Clinic seeks to provide the best possible medical care, surgical care and dental care for their highly-valued patients. We are committed to promoting responsible pet ownership, preventative health care and health-related educational opportunities for our clients.</p>
</section>

<footer class="abs site-footer">
  <div class="footer-links">Site Map HOME| ABOUT| NEWS/EVENTS| FAQS| CONTACT|<br>Copyright © 2014 All rights reserved.</div>
  <span class="social" style="left:524px;background:#3a7fa8"></span>
  <span class="social" style="left:559px;background:#4a9fd0"></span>
  <span class="social" style="left:594px;background:#d9b233"></span>
  <span class="social" style="left:629px;background:#c4513f"></span>
  <span class="to-top">↑</span>
</footer>

</body>
</html>
```